Business Card Design REAL ESTATE SALES PLEASE DESIGN MY CARD 2COLOR CARD WITH RED AS THE DOMINANT

FERNHOLM REALTY
TorLPA Lic# 04738216
RAFAEL " RAFE " MORTON Tel 555 218-3396
TorLPA Lic# 02864057 Fax 555 218-3740
Email: rafe@rafemortonhomes.net Cell 555 902-4481
47530 WREN TERRACE UNION CITY, CA 94312

RAFAEL " RAFE " MORTON
TEL: 555 218-3396 FAX 555 218-3740
Address: 47530 Wren Terrace Alder Bay , OR
EMAIL ADDRESS: rafe@rafemortonhomes.net

```html
<!DOCTYPE html>
<html lang="en">
<head>
<meta charset="utf-8">
<title>Fernholm Realty – Business Card</title>
<link rel="stylesheet" href="https://fonts.googleapis.com/css2?family=Open+Sans:wght@400;600&display=swap">
<style>
  :root {
    --stage: #1c1c1c;
    --paper: #ffffff;
    --charcoal-light: #4a4a4a;
    --charcoal-dark: #2b2b2b;
    --red: #d71f32;
    --red-dark: #a3111f;
    --ink: #3a3a3a;
    --tab: #1a1a1a;
    --logo-text: #e8e8e8;
    --logo-sub: #9a9a9a;
  }
  * { margin: 0; padding: 0; box-sizing: border-box; }
  html, body {
    width: 1200px; height: 675px; overflow: hidden;
    background: var(--stage);
    font-family: "Open Sans", sans-serif;
  }
  .canvas {
    position: relative; width: 1200px; height: 675px;
    display: flex; align-items: center; justify-content: center;
  }
  .card {
    position: relative; width: 840px; height: 480px;
    background: var(--paper);
    overflow: hidden;
    box-shadow: 0 18px 40px rgba(0,0,0,.55);
  }
  .card-shapes { position: absolute; inset: 0; }
  .contact-list {
    position: absolute; left: 118px; top: 150px;
    list-style: none;
    color: var(--ink);
    font-size: 15px; font-weight: 600;
    letter-spacing: 1.6px; line-height: 1.45;
  }
  .contact-item { position: absolute; left: 0; white-space: nowrap; }
  .contact-item--phone { top: 0; }
  .contact-item--email { top: 78px; }
  .contact-item--address { top: 160px; }
  .brand {
    position: absolute; left: 560px; top: 205px;
    width: 260px; text-align: center;
  }
  .brand-name {
    color: var(--logo-text);
    font-size: 27px; font-weight: 400;
    letter-spacing: 0.5px; line-height: 1;
  }
  .brand-agent {
    margin-top: 8px;
    color: var(--logo-sub);
    font-size: 10px; font-weight: 400;
    letter-spacing: 3px;
  }
</style>
</head>
<body>
<main class="canvas">
  <article class="card">
    <svg class="card-shapes" width="840" height="480" viewBox="0 0 840 480" aria-hidden="true">
      <defs>
        <linearGradient id="panelShade" x1="0" y1="0" x2="1" y2="1">
          <stop offset="0" stop-color="var(--charcoal-light)"/>
          <stop offset="1" stop-color="var(--charcoal-dark)"/>
        </linearGradient>
        <linearGradient id="bandShade" x1="0" y1="0" x2="1" y2="0">
          <stop offset="0" stop-color="var(--red)"/>
          <stop offset="1" stop-color="var(--red-dark)"/>
        </linearGradient>
      </defs>
      <polygon class="accent-band" points="318,0 378,0 378,30 548,430 548,480 520,480 352,70 318,30" fill="url(#bandShade)"/>
      <polygon class="brand-panel" points="378,0 840,0 840,480 548,480 548,430 378,30" fill="url(#panelShade)"/>
      <polygon class="icon-tab" points="0,20 30,20 58,52 58,480 0,480" fill="var(--tab)"/>
      <g class="icon icon-phone" transform="translate(54,172)">
        <rect x="-18" y="-18" width="36" height="36" rx="8" fill="var(--tab)"/>
        <path d="M-7,-8 q-3,2 -1,7 q4,8 12,11 q4,1 6,-2 l-4,-4 q-2,1 -3,1 q-4,-2 -6,-6 q0,-1 1,-3 z" fill="#fff"/>
      </g>
      <g class="icon icon-globe" transform="translate(54,252)" fill="none" stroke="#fff" stroke-width="1.6">
        <rect x="-18" y="-18" width="36" height="36" rx="8" fill="var(--tab)" stroke="none"/>
        <circle r="9"/>
        <ellipse rx="4" ry="9"/>
        <line x1="-9" y1="0" x2="9" y2="0"/>
        <line x1="-8" y1="-4.5" x2="8" y2="-4.5"/>
        <line x1="-8" y1="4.5" x2="8" y2="4.5"/>
      </g>
      <g class="icon icon-pin" transform="translate(54,334)">
        <rect x="-18" y="-18" width="36" height="36" rx="8" fill="var(--tab)"/>
        <path d="M0,10 L-6,0 A7,7 0 1 1 6,0 Z" fill="#fff"/>
        <circle cx="0" cy="-4" r="2.6" fill="var(--tab)"/>
      </g>
    </svg>

    <ul class="contact-list">
      <li class="contact-item contact-item--phone">555 218-3396<br>FAX 555 218-3740</li>
      <li class="contact-item contact-item--email">rafe@rafemortonhomes.net</li>
      <li class="contact-item contact-item--address">47530 Wren Terrace Alder Bay , OR</li>
    </ul>

    <div class="brand">
      <div class="brand-name">FERNHOLM REALTY</div>
      <div class="brand-agent">RAFAEL · RAFE · MORTON</div>
    </div>
  </article>
</main>
</body>
</html>
```